Stationery Design Project

Hi All,

We need you to design stationary for a new Business and Accounting Advisory Firm. We have already got the logo designed and it is attached. If you could also if possible, match the fonts in your design to that on the logo’s provided.

What we need:
- Business Card
- A4 Letter head
- A4 Folders
- PPT template (Title page and regular page)

And what ever else you want to throw in.

We are in the process of getting the web site designed, however below is a list of websites which we like which will give you an understanding of the style that we are going for.

- plavoni.com
- brightfunnelo.com
- hourquillet.com
- artmarrowly.com

I look forward to your seeing your design.

Hi All,

I have just realised that I forgot that i need to include a Licensed Tallymasters image on the letter head, please find attaced as File 1. Could you please have this image in the bottom left header.

Regards,

Gareth

Industry/Entity Type

Business

Requirements
Must have
• Outputs:
- Documents ready to print
- Generic editable information
- Pdf copies of the documents
- Word version of letterhead

```html
<!DOCTYPE html>
<html lang="en">
<head>
<meta charset="utf-8">
<title>Orrindale Group — Business Card Set</title>
<link href="https://fonts.googleapis.com/css2?family=Tinos:wght@400;700&display=swap" rel="stylesheet">
<style>
  :root {
    --backdrop: #8a8d90;
    --paper: #ffffff;
    --ink-dark: #2f2f2f;
    --night: #030303;
    --brand-blue: #34518f;
    --accent-orange: #f2a23a;
    --gold: #f4c54a;
    --band-top: #4a9fd6;
    --band-bottom: #3b62ad;
    --panel-blue: #3a5ea2;
    --panel-glow: #45b6de;
    --white: #ffffff;
  }
  * { box-sizing: border-box; margin: 0; padding: 0; }
  html, body { width: 1200px; height: 709px; overflow: hidden; background: var(--backdrop); }
  .sheet { position: relative; width: 1200px; height: 709px; }

  .card {
    position: absolute; width: 558px; height: 319px; overflow: hidden;
    border: 1px solid #5a5d60;
  }
  .card--front-light { left: 29px; top: 19px; background: var(--paper); }
  .card--front-dark  { left: 617px; top: 19px; background: var(--night); }
  .card--back-light  { left: 33px; top: 363px; background: var(--paper); }
  .card--back-blue   {
    left: 615px; top: 363px;
    background: radial-gradient(circle at 48% 54%, var(--panel-glow) 0%, #3f80c4 28%, var(--panel-blue) 62%);
  }

  /* company name */
  .company-name {
    position: absolute; left: 0; right: 0; text-align: center;
    font-family: "Tinos", serif; font-weight: 400; font-size: 36px; line-height: 1;
    color: var(--brand-blue); white-space: nowrap;
  }
  .card--front-light .company-name, .card--front-dark .company-name { top: 72px; }
  .card--back-light .company-name { top: 140px; }

  /* contact band */
  .rule { position: absolute; left: 0; right: 0; top: 198px; height: 3px; background: var(--accent-orange); }
  .band {
    position: absolute; left: 0; right: 0; top: 201px; bottom: 0;
    background: linear-gradient(180deg, var(--band-top), var(--band-bottom));
  }
  .band__divider { position: absolute; left: 243px; top: 12px; width: 1px; height: 96px; background: rgba(255,255,255,.75); }
  .band__left {
    position: absolute; right: 332px; text-align: right; color: var(--white);
    font-family: "Tinos", serif;
  }
  .person__name { font-weight: 700; font-size: 22px; line-height: 1.1; }
  .person__role { font-size: 17px; line-height: 1.3; }
  .card--front-light .band__left { top: 34px; }
  .card--front-dark .band__left { top: 30px; font-size: 18px; line-height: 23px; }

  .contacts { position: absolute; left: 258px; top: 15px; list-style: none; }
  .contacts li {
    display: flex; align-items: center; gap: 7px; height: 23.5px;
    font-family: "Tinos", serif; font-size: 17.5px; color: var(--white);
  }
  .contacts svg { width: 13px; height: 13px; flex: none; fill: var(--white); }

  .address-line {
    position: absolute; left: 0; right: 0; top: 175px; text-align: center;
    font-family: "Tinos", serif; font-size: 17.5px; color: var(--ink-dark);
  }
  .dark-name {
    position: absolute; left: 0; right: 0; top: 167px; text-align: center;
    font-family: "Tinos", serif; color: var(--gold);
  }
  .dark-name strong { font-size: 22px; }
  .dark-name span { font-size: 17px; }

  .web-line {
    position: absolute; left: 0; right: 0; text-align: center;
    font-family: "Tinos", serif; font-size: 19px; letter-spacing: 1.6px;
  }
  .card--back-light .web-line { top: 255px; color: var(--night); }
  .card--back-blue .web-line { top: 288px; color: var(--white); font-size: 18px; }

  .hero-name {
    position: absolute; left: 0; right: 0; top: 120px; text-align: center;
    font-family: "Tinos", serif; font-weight: 400; font-size: 50px; color: var(--white);
  }
</style>
</head>
<body>
<svg width="0" height="0" style="position:absolute">
  <defs>
    <symbol id="icon-phone" viewBox="0 0 16 16"><path d="M3.5 1.5l2.5 0 1 3.5-1.8 1.2a8 8 0 0 0 4.6 4.6L11 9l3.5 1v2.5c0 1-1 2-2 2A11 11 0 0 1 1.5 3.5c0-1 1-2 2-2z"/></symbol>
    <symbol id="icon-fax" viewBox="0 0 16 16"><path d="M4 2h8v4H4zM1.5 6.5h13v6h-2v-2h-9v2h-2zM4 11.5h8v3H4z"/></symbol>
    <symbol id="icon-mail" viewBox="0 0 16 16"><path d="M1 5l7-3.5L15 5v9H1zM2.5 6l5.5 4 5.5-4v-.3L8 3.2 2.5 5.7z"/></symbol>
    <symbol id="icon-globe" viewBox="0 0 16 16"><path d="M8 1a7 7 0 1 0 0 14A7 7 0 0 0 8 1zm0 1.5c.8 0 1.7 1.9 1.9 4.7H6.1C6.3 4.4 7.2 2.5 8 2.5zM2.6 8.8h2.1c.1 1.8.5 3.3 1 4.3a5.5 5.5 0 0 1-3.1-4.3zm0-1.6a5.5 5.5 0 0 1 3.1-4.3c-.5 1-.9 2.5-1 4.3zm3.5 1.6h3.8C9.7 11.6 8.8 13.5 8 13.5S6.3 11.6 6.1 8.8zm5.2 0h2.1a5.5 5.5 0 0 1-3.1 4.3c.5-1 .9-2.5 1-4.3zm0-1.6c-.1-1.8-.5-3.3-1-4.3a5.5 5.5 0 0 1 3.1 4.3z"/></symbol>
  </defs>
</svg>

<main class="sheet">
  <section class="card card--front-light">
    <p class="company-name">Orrindale Group</p>
    <p class="address-line">Street Name, City Name, State, City Zip Code</p>
    <div class="rule"></div>
    <div class="band">
      <div class="band__left">
        <p class="person__name">Your Name</p>
        <p class="person__role">Designation</p>
      </div>
      <div class="band__divider"></div>
      <ul class="contacts">
        <li><svg><use href="#icon-phone"/></svg>0123-456-789</li>
        <li><svg><use href="#icon-fax"/></svg>0123-456-789</li>
        <li><svg><use href="#icon-mail"/></svg>info@orrindalegroup.com</li>
        <li><svg><use href="#icon-globe"/></svg>www.orrindalegroup.com</li>
      </ul>
    </div>
  </section>

  <section class="card card--front-dark">
    <p class="company-name">Orrindale Group</p>
    <p class="dark-name"><strong>Your Name,</strong> <span>Designation</span></p>
    <div class="rule"></div>
    <div class="band">
      <div class="band__left">
        <p>Street Name</p>
        <p>City Name</p>
        <p>State, City Zip Code</p>
      </div>
      <div class="band__divider"></div>
      <ul class="contacts">
        <li><svg><use href="#icon-phone"/></svg>0123-456-789</li>
        <li><svg><use href="#icon-fax"/></svg>0123-456-789</li>
        <li><svg><use href="#icon-mail"/></svg>info@orrindalegroup.com</li>
        <li><svg><use href="#icon-globe"/></svg>www.orrindalegroup.com</li>
      </ul>
    </div>
  </section>

  <section class="card card--back-light">
    <p class="company-name">Orrindale Group</p>
    <p class="web-line">www.orrindalegroup.com</p>
  </section>

  <section class="card card--back-blue">
    <p class="hero-name">Orrindale Group</p>
    <p class="web-line">www.orrindalegroup.com</p>
  </section>
</main>
</body>
</html>
```